Newsletter-Design für Print - tornhof partner
Zielgruppe
tornhof partner business hat sich auf die Kaltakquise und den Vertrieb spezialisiert. Generell agieren wir ausschließlich im BtoB Bereich überwiegend für die Industrie.
Aufgabenstellung
verwenden unserer Logofarben - Blau und Rot - maximal noch grau - sehr puristisch und minimalistisch - klare Struktur für case studiens - checklisten - whitepapers

```html
<!DOCTYPE html>
<html lang="de">
<head>
<meta charset="utf-8">
<title>Newsletter 03|2017 – tornhof partner</title>
<link href="https://fonts.googleapis.com/css2?family=Open+Sans:wght@400;600;700&display=swap" rel="stylesheet">
<style>
:root{
  --stage:#8c8c8c;
  --paper:#ffffff;
  --panel:#dcdcdc;
  --red:#b3342c;
  --blue:#2d4f86;
  --bar:#4d6b9c;
  --text:#555555;
  --muted:#c8c8c8;
  --white:#ffffff;
}
*{box-sizing:border-box;margin:0;padding:0}
html,body{width:1200px;height:2339px;overflow:hidden}
body{background:var(--stage);font-family:"Open Sans",Arial,sans-serif;color:var(--text);position:relative}
.page{position:absolute;width:480px;height:679px;background:var(--paper);box-shadow:0 4px 14px rgba(0,0,0,.35)}
.panel{position:absolute;left:9px;top:9px;width:462px;height:613px;background:var(--panel)}
.abs{position:absolute}
.headline-red{color:var(--red);font-weight:600;text-transform:uppercase;font-size:23.5px;line-height:28px;white-space:nowrap}
.headline-blue{color:var(--blue);font-weight:600;text-transform:uppercase;font-size:23.5px;line-height:28px;text-align:right;white-space:nowrap}
.cover-label{color:var(--white);font-size:16px;letter-spacing:.2px}
.toc{list-style:none;color:var(--white);font-size:15.5px;line-height:16px}
.toc li{display:flex;margin-bottom:7px}
.toc .num{width:36px}
.toc .entry{border-left:1px solid var(--white);padding-left:6px}
.brand{color:var(--blue);font-weight:600;font-size:19px;letter-spacing:.3px}
.lead{color:var(--text);font-size:10.3px;line-height:14.5px;text-transform:uppercase;text-align:justify}
.lead.light{color:var(--white);font-weight:600}
.body{font-size:10.3px;line-height:14.5px;text-align:justify}
.item{position:absolute;display:flex;gap:11px}
.item .icon{flex:none;width:17px;height:17px;border-radius:3px;background:var(--red);color:var(--white);font-weight:700;font-size:13px;line-height:17px;text-align:center;margin-top:2px}
.item h4{color:var(--white);font-size:10.3px;line-height:14.5px;font-weight:600;text-transform:uppercase}
.item p{font-size:10.3px;line-height:14.5px}
.photo{position:absolute}
.footer{position:absolute;top:640px;font-size:12px;color:var(--muted);display:flex;align-items:baseline;gap:10px}
.footer b{font-size:22px;font-weight:400}
.chart{position:absolute;left:0;top:412px;width:480px;height:160px}
.row{position:absolute;left:0;width:480px;height:17px}
.row .lbl{position:absolute;left:0;top:0;width:140px;text-align:right;font-size:9px;line-height:17px;color:var(--blue);text-transform:uppercase;white-space:nowrap}
.row .plus{position:absolute;left:148px;top:0;width:17px;height:17px;background:var(--blue);color:var(--white);font-weight:700;font-size:14px;line-height:17px;text-align:center;border-radius:2px}
.row .bar{position:absolute;left:170px;top:0;height:17px;background:var(--bar);color:var(--white);font-size:12px;font-weight:600;padding-left:10px;line-height:17px}
.quote-mark{color:var(--blue);font-size:56px;font-weight:700;line-height:40px}
.quote{font-size:10.3px;line-height:14.5px;color:var(--text);text-transform:uppercase;text-align:justify}
.stat{position:absolute;width:130px;text-align:center}
.stat .circle{width:90px;height:90px;margin:0 auto;border-radius:50%;background:var(--blue);color:var(--white);font-size:32px;font-weight:600;line-height:90px}
.stat h5{color:var(--blue);font-size:10.5px;font-weight:600;margin-top:12px}
.stat p{color:var(--blue);font-size:9px;line-height:10.5px;margin-top:6px}
</style>
</head>
<body>

<!-- Cover -->
<section class="page" style="left:598px;top:78px">
  <div class="panel"></div>
  <div class="abs cover-label" style="left:41px;top:40px">NEWSLETTER 03|2017</div>
  <h1 class="abs headline-red" style="left:41px;top:137px">Iquo consequia saectur<br>se etus dipsum volupta<br>turemqu iderum conseque<br>es nis quas dolupta ssento<br>occaborumqui omniminum<br>nimus delectur.</h1>
  <ol class="abs toc" style="left:41px;top:384px">
    <li><span class="num">02</span><span class="entry">Em essima quatur<br>volorum nimolum</span></li>
    <li><span class="num">04</span><span class="entry">Simenet autemodi cum<br>quat volorerrum ium</span></li>
    <li><span class="num">05</span><span class="entry">Etusda ius et assimus</span></li>
    <li><span class="num">06</span><span class="entry">Aatiorati volu Imos<br>sendae cum recerferum</span></li>
    <li><span class="num">07</span><span class="entry">Faceriatur volorerrum</span></li>
  </ol>
  <div class="abs brand" style="right:16px;top:636px">tornhof partner</div>
</section>

<!-- Page 02 -->
<section class="page" style="left:117px;top:827px">
  <div class="panel"></div>
  <div class="abs" style="left:9px;top:9px;width:232px;height:282px;background:linear-gradient(180deg,#e4e4e4,#f2f2f2)"></div>
  <div class="photo" role="img" aria-label="Porträtfoto einer Beraterin am Schreibtisch, schwarz-weiß" style="left:241px;top:9px;width:230px;height:282px;background:linear-gradient(135deg,#9a9a9a,#3a3a3a 70%,#e8e8e8)"></div>
  <h2 class="abs headline-red" style="left:36px;top:40px">Magnimus qui<br>depro eos ethil</h2>
  <p class="abs lead" style="left:37px;top:132px;width:187px">Bearchitatis et queni earcien daeped minum que et volorum sum alib dunt earum, unt est pos utemvollaud igentem posti untur? Occum hiliatur? Qui dolo con rem laccuptam in pra dipietur, ut lam reet erum autrema aliti dit</p>
  <div class="item" style="left:39px;top:319px;width:383px"><span class="icon">?</span><div><h4>Vid quia doluptisquam sequia iliqui omnimol uptatqu untur net et eum dolupid qui dis?</h4><p>Quas adionsequo corrum as vid qui idici berumet destia dus, offictus, si occaecu llamus endiaspiet ommoles truptaepudis cusa cus.</p></div></div>
  <div class="item" style="left:39px;top:395px;width:383px"><span class="icon">?</span><div><h4>Sim rehente omnis peris am, ita porem qui in net et eum dolupid qui dis ad que rat ad ullam qui in net et eum dolupid?</h4><p>Idi si veleste et ab ipiciis nis sitasitat Is qui odi re porum que cusam, ipsa coreria spelit voluptiunt la qui re veliqui aut alit aliae estem iduciis Nus, simolor eribus esciis magnam hit estisque dolecum harchil in porporr umquasp idebis eos Sinulparit.</p></div></div>
  <div class="item" style="left:39px;top:501px;width:383px"><span class="icon">?</span><div><h4>Nempel eumharum aditas ita porem ad que rat ad ullam qui adut teod ita porem ad que rat ad ullam qui iliqui omnimol uptatqu untur net et eum dolupid?</h4><p>Eveniae laborepudit, quid quo quibusdae quiam es reptatiam eaqui natquia venimag natiati onsequi volorem nianturio et fugia con restia ventium faciam, omniae. Dis mossim abor sum quo eosaepellit, qui odia dest unt, sum liatibus quiam, ut por raeptas non cusdae preicie.</p></div></div>
  <div class="footer" style="left:15px"><b>02</b>NEWSLETTER 03|2017</div>
</section>

<!-- Page 03 -->
<section class="page" style="left:598px;top:827px">
  <div class="panel"></div>
  <h2 class="abs headline-blue" style="right:39px;top:40px">At earume haritas pro comnis<br>rem quosam landae</h2>
  <div class="abs" style="left:36px;top:132px;width:197px">
    <p class="lead light">Et venda eum, same id quiasinvero bea nonectium, voluptasiti dellicae. Ita pra iur, con ratem que dentur autatiusant dolupta doluptatem inverum erum doluptaque quiam sandendunt esasum harundus simus.</p>
    <p class="body" style="margin-top:14px">Eati conseque voluptatus, ut exero modipsuntio ipitas inctotat optiistis imint et quatemp orecus imporis eos apidebitatur soloreptat. Nulpariorro miniet verio. Am iur, consecu ptatur? Ellaces cum fugi-</p>
  </div>
  <p class="abs body" style="left:245px;top:132px;width:197px">as autatas quae. Aquo eaquata endenec earibusant, enimusam qui ipsus. Ceaturepedis ni iusdae nonseque nihil etur adi ut et est landic te laut eius dolor sundunto veliqui aut et eaturibust. Veliqui beatem dolum iunto omnis eiur, comniet eos doleculles maiorum quatquia versped. Ebitatque conectur abor sum vent eum untus ese que aut lautatur accusame cum ute evelest iuscit officime doloria tecatis volum ent ommos estrum quam que nosam, eatemperis eicid ma dello tectis maxim quam anit.</p>
  <p class="abs lead light" style="left:36px;top:358px;width:406px">Reius, ipsam, int, optatem quisserunten qui sapis doloria sitaecte essimil idia diaeratiossi ditiae nullore nihic tent, ut et volorep elibus et ant aut aut et repudam, ommodit mo volesti .</p>
  <div class="chart">
    <div class="row" style="top:0"><span class="lbl">Cimagnatatem hiliqu</span><span class="plus">+</span><span class="bar" style="width:161px">236</span></div>
    <div class="row" style="top:23px"><span class="lbl">Tum aut paria</span><span class="plus">+</span><span class="bar" style="width:226px">355</span></div>
    <div class="row" style="top:46px"><span class="lbl">Doluptaturem aut</span><span class="plus">+</span><span class="bar" style="width:210px">308</span></div>
    <div class="row" style="top:69px"><span class="lbl">Rum quatur agnimpe</span><span class="plus">+</span><span class="bar" style="width:240px">370</span></div>
    <div class="row" style="top:92px"><span class="lbl">Mus berias dolorat</span><span class="plus">+</span><span class="bar" style="width:250px">380</span></div>
    <div class="row" style="top:115px"><span class="lbl">Ris eatiaectia autem</span><span class="plus">+</span><span class="bar" style="width:270px">423</span></div>
    <div class="row" style="top:138px"><span class="lbl">Facessunt volorro</span><span class="plus">+</span><span class="bar" style="width:224px">315</span></div>
  </div>
  <div class="footer" style="right:15px"><span>NEWSLETTER 03|2017</span><b>03</b></div>
</section>

<!-- Page 04 -->
<section class="page" style="left:117px;top:1579px">
  <div class="panel"></div>
  <h2 class="abs headline-red" style="left:36px;top:40px">Iquo consequia saectur<br>se etus dipsum volupta</h2>
  <p class="abs lead light" style="left:37px;top:133px;width:137px">Bearchitatis et queni earcien daeped minum que et volorum sum alib dunt earum, unt est pos utemvollaud igentem posti untur? Occum hiliatur? Qui dolo con rem laccuptam in pra dipietur, ut lam reet erum autrema aliti dit</p>
  <div class="item" style="left:207px;top:133px;width:232px"><span class="icon">+</span><div><h4>Vid quia doluptisquam sequia iliqui omnimol uptatqu untur</h4><p>Quas adionsequo corrum as vid qui idici berumet destia dus, offictus, si occaecu llamus endiaspiet ommoles truptaepudis cusa cus.</p></div></div>
  <div class="item" style="left:207px;top:240px;width:232px"><span class="icon">+</span><div><h4>Sim rehente omnis peris am, in net et eum dolupid qui dis</h4><p>Idi si veleste et ab ipiciis nis sitasitat Is qui odi re porum que cusam, ipsa coreria spelit voluptiunt la qui re veliqui aut alit aliae estem iduciis Nus, simolor eribus esciis magnam hit estisque dolecum harchil in porporr umquasp idebis eos Sinulparit.</p></div></div>
  <div class="item" style="left:207px;top:373px;width:232px"><span class="icon">+</span><div><h4>Nempel eumharum aditas<br>adut teod</h4><p>Eveniae laborepudit, quid quo quibusdae quiam es reptatiam eaqui natquia venimag natiati onsequi volorem nianturio et fugia con restia ventium faciam, omniae.</p></div></div>
  <div class="item" style="left:207px;top:479px;width:232px"><span class="icon">+</span><div><h4>Ita porem ad que rat ad ullam qui</h4><p>Dis mossim abor sum quo eosaepellit, qui odia dest unt, sum liatibus quiam, ut por raeptas non cusdae preicie ndigni ideleni­mus etur archillor se corem.</p></div></div>
  <div class="footer" style="left:15px"><b>04</b>NEWSLETTER 03|2017</div>
</section>

<!-- Page 05 -->
<section class="page" style="left:598px;top:1579px">
  <div class="panel"></div>
  <h2 class="abs headline-blue" style="right:39px;top:40px">Tinven dendit facca<br>ndipicid nemoluptur</h2>
  <div class="photo" role="img" aria-label="Hintergrundfoto Büro, hell, schwarz-weiß" style="left:9px;top:107px;width:462px;height:283px;background:linear-gradient(90deg,#cfcfcf,#f2f2f2 60%,#e0e0e0)"></div>
  <div class="photo" role="img" aria-label="Porträtfoto eines Mannes mit Brille und Weste, schwarz-weiß" style="left:9px;top:107px;width:247px;height:283px;background:linear-gradient(160deg,#bdbdbd,#4a4a4a 60%,#8a8a8a)"></div>
  <div class="abs quote-mark" style="left:270px;top:125px">”</div>
  <p class="abs quote" style="left:270px;top:164px;width:170px">Tet quatus dolorep rovitioreped explis digende moluptatqui cori tem reprepeles quias aut eium inimporectae porestium eaquibus sim ad utatem fugitatempe non consequis repel ipsunt. Xime sus soluptatem hicit.</p>
  <p class="abs lead light" style="left:39px;top:403px;width:402px">Quibus as est, autenih illiae serspero blam ipsam, ut hicabor sitias dolore, sum et et verum eici velectu rerovid et excerciliquo.</p>
  <div class="stat" style="left:37px;top:450px"><div class="circle">295</div><h5>OR SEQUI RES</h5><p>Nem iunt ium fu-<br>gia iuscide<br>liquatureped.</p></div>
  <div class="stat" style="left:176px;top:450px"><div class="circle">324</div><h5>OCCAECTOT</h5><p>Reperendem rese-<br>quisci con rerum<br>ex et odi.</p></div>
  <div class="stat" style="left:314px;top:450px"><div class="circle">855</div><h5>EMPORUPT</h5><p>Os unt que mo-<br>lupic te de nobis<br>acernam quiberi.</p></div>
  <div class="footer" style="right:15px"><span>NEWSLETTER 03|2017</span><b>05</b></div>
</section>

</body>
</html>
```